FLyer for Malaysia's No. 1 Healthcare Job Site (name of job site: Vireta)

Objective of flyer - to get people to register on the job site
Must have:
Logo and Name (Vireta)
Tagline: Malaysia's #1 Healthcare Job site
url: www.vireta-jobs.example
social media links
FB:Vireta
LinkedIn: viretajobs
Instagram: @viretajobs

WE cover the entire healthcare industry areas (doctors, nurses, dentists, pharmacists, psychologists, administrative staff, biomedical engineers....etc)

Please remember that our focus service is our Job-site, we want people to realize in the first look that we are a healthcare Job site.

Flyer size: A5

Color code: #279582 (80%) & #96c836 (20%)

Target Market(s)

All Healthcare Professionals in Malaysia

Industry/Entity Type

Healthcare

Requirements
Must have
• Web site: www.vireta-jobs.example
• Logo and Tagline (attached)
• 2 side design
• Really important (Our Product is our Job site)
Nice to have
• Asian Healthcare professionals, info graphic icons.

```html
<!DOCTYPE html>
<html lang="en">
<head>
<meta charset="utf-8">
<title>Vireta — A5 Flyer</title>
<link href="https://fonts.googleapis.com/css2?family=Source+Sans+3:ital,wght@0,400;0,600;0,700;1,600&display=swap" rel="stylesheet">
<style>
:root{
  --teal:#279582;
  --teal-hero:#2a8f9c;
  --green:#96c836;
  --slate:#33434b;
  --ink:#222;
  --grey:#555;
  --paper:#fff;
  --bg:#ebe7e2;
}
*{box-sizing:border-box;margin:0;padding:0}
html,body{width:1200px;height:1200px;overflow:hidden}
body{background:var(--bg);font-family:"Source Sans 3",sans-serif;color:var(--ink);position:relative}
.page{position:absolute;top:218px;width:540px;height:764px;background:var(--paper);overflow:hidden;box-shadow:0 6px 18px rgba(0,0,0,.18)}
.page--front{left:40px}
.page--back{left:620px}
.abs{position:absolute}

/* front: header */
.header{left:0;top:0;width:540px;height:149px;background:linear-gradient(90deg,#fff 0%,#f1f6f5 40%,#bfe2dc 100%)}
.header-logo{left:40px;top:44px;display:flex;align-items:center;gap:10px;color:var(--teal);font-size:50px;font-weight:400;letter-spacing:1px}
.dot{width:14px;height:14px;border-radius:50%;background:var(--teal)}

/* front: hero */
.hero{left:0;top:149px;width:540px;height:190px;background:linear-gradient(90deg,#fff 0%,#cfe9ea 22%,#3d9fae 52%,var(--teal-hero) 100%)}
.hero-photo{left:163px;top:29px;width:95px;height:161px;background:linear-gradient(180deg,#e9eef0,#c9d5d8);border-radius:4px}
.hero-copy{right:33px;top:36px;text-align:right;font-weight:700;font-size:20px;line-height:24px;color:#fff}
.hero-copy .kicker{color:var(--green)}
.hero-copy .slash{color:var(--green);font-weight:400;font-size:26px;margin:0 2px}
.btn-signup{left:429px;top:136px;width:77px;height:28px;background:var(--green);color:#fff;font-weight:600;font-size:15px;display:flex;align-items:center;justify-content:center}

/* front: search */
.search{left:0;top:339px;width:540px;height:79px;background:var(--slate)}
.search-icon{left:39px;top:22px;width:38px;height:37px;background:#fff;border-radius:4px;display:flex;align-items:center;justify-content:center}
.search-field{left:86px;top:22px;width:280px;height:37px;background:#eceeef;border-radius:3px 0 0 3px;font-size:15.5px;color:#444;display:flex;align-items:center;padding-left:34px}
.search-url{left:355px;top:22px;width:150px;height:37px;background:var(--green);clip-path:polygon(0 0,100% 0,100% 100%,12px 100%,0 0);font-size:12.5px;color:#2d3a30;display:flex;align-items:center;justify-content:flex-end;padding-right:8px;border-radius:0 3px 3px 0}

/* front: audience blocks */
.circle{border-radius:50%;border:4px solid #fff;box-shadow:0 2px 8px rgba(0,0,0,.35)}
.photo-jobseeker{left:49px;top:435px;width:124px;height:124px;background:linear-gradient(135deg,#c9d0d6,#6f7c86)}
.photo-employer{left:380px;top:544px;width:120px;height:120px;background:linear-gradient(135deg,#e7eef3,#9eb2c4)}
.block-title{color:var(--teal);font-weight:700;font-size:29px;line-height:32px}
.block-text{font-size:16.5px;line-height:21px;color:var(--ink)}
.jobseekers{left:185px;top:455px}
.employers{right:178px;top:560px;text-align:right}

/* shared footer */
.footer{left:0;top:680px;width:540px;height:84px;background:var(--slate);color:#fff}
.footer-logo{left:36px;top:20px;font-size:34px;line-height:40px;letter-spacing:1px;display:flex;align-items:center;gap:8px}
.footer-logo .dot{background:#fff;width:10px;height:10px}
.footer-rule{left:225px;top:24px;width:1.5px;height:40px;background:#fff}
.footer-info{left:289px;top:17px;font-size:11.5px;line-height:17px}
.footer-info .tag{font-weight:700;font-size:9.5px}
.social{display:inline-flex;align-items:center;gap:3px;margin-right:9px}
.social i{display:inline-block;width:7px;height:7px;background:#fff}

/* back: intro */
.intro-mark{left:46px;top:66px;width:70px;display:flex;flex-direction:column;align-items:center;gap:10px;color:var(--teal);font-size:20px;font-weight:600}
.intro-mark .dot{width:62px;height:62px}
.intro{left:143px;top:56px;width:353px;font-size:15px;line-height:20px;text-align:justify}
.intro p+p{margin-top:20px}
.hl{color:var(--teal);font-weight:700}

/* back: professions */
.pro{left:0;top:306px;width:540px;height:374px;background:var(--teal);color:#fff;text-align:center}
.pro-title{left:0;top:46px;width:540px;font-weight:700;font-size:27.5px;line-height:36px}
.pro-photo{top:140px;width:112px;height:112px}
.p1{left:28px;background:linear-gradient(135deg,#e3e8ec,#8b9aa6)}
.p2{left:152px;background:linear-gradient(135deg,#f2c58f,#eef1f3)}
.p3{left:276px;background:linear-gradient(135deg,#d9e4e4,#c39a7e)}
.p4{left:400px;background:linear-gradient(135deg,#dfeaf1,#9fb7c9)}
.pro-text{left:0;top:280px;width:540px;font-size:19px;line-height:25px}
</style>
</head>
<body>

<section class="page page--front">
  <div class="abs header" role="img" aria-label="Faded photo of smiling healthcare staff"></div>
  <div class="abs header-logo"><span class="dot"></span>Vireta</div>

  <div class="abs hero">
    <div class="abs hero-photo" role="img" aria-label="Photo of a doctor in a white coat looking through binoculars"></div>
    <div class="abs hero-copy">
      <div class="kicker">healthcare</div>
      <div>Malaysia’s #1 <span class="slash">/</span>job site</div>
    </div>
    <div class="abs btn-signup">Sign Up</div>
  </div>

  <div class="abs search">
    <div class="abs search-icon">
      <svg width="22" height="22" viewBox="0 0 22 22" fill="none" stroke="#222" stroke-width="2.2"><circle cx="9" cy="9" r="6.5"/><line x1="14" y1="14" x2="20" y2="20" stroke-linecap="round"/></svg>
    </div>
    <div class="abs search-field">Search healthcare jobs here!</div>
    <div class="abs search-url">www.<b>vireta-jobs</b>.example</div>
  </div>

  <div class="abs circle photo-jobseeker" role="img" aria-label="Photo of a jobseeker working at a computer"></div>
  <div class="abs jobseekers">
    <div class="block-title">Jobseekers</div>
    <div class="block-text">In just 3 easy steps,<br>find your dream Healthcare job!</div>
  </div>

  <div class="abs employers">
    <div class="block-title">Employers</div>
    <div class="block-text">We’ve made <i style="font-weight:600">Talent Recruitment</i><br>more convenient and time efficient for you</div>
  </div>
  <div class="abs circle photo-employer" role="img" aria-label="Photo of a hospital ward with a bed and monitors"></div>

  <div class="abs footer">
    <div class="abs footer-logo"><span class="dot"></span>Vireta</div>
    <div class="abs footer-rule"></div>
    <div class="abs footer-info">
      <div class="tag">Malaysia’s #1 healthcare job site</div>
      <div><span class="social"><i></i>Vireta</span><span class="social"><i></i>viretajobs</span><span class="social"><i></i>@viretajobs</span></div>
      <div>www.vireta-jobs.example</div>
    </div>
  </div>
</section>

<section class="page page--back">
  <div class="abs intro-mark"><span class="dot"></span>Vireta</div>
  <div class="abs intro">
    <p>We are <span class="hl">Malaysia’s #1 Healthcare Job Site</span> fully dedicated to the healthcare industry, being a part of the new generation of Job Sites worldwide.</p>
    <p>Our jobs cover niche Healthcare Vacancies - connecting you to the right employers. Use VIRETA to create your CV, search for specific jobs, survey market salary ranges and most importantly, <span class="hl">gain access to a growing network of local and international Healthcare Employers.</span></p>
  </div>

  <div class="abs pro">
    <div class="abs pro-title">Are you a Doctor? A Nurse?<br>A Pharmacist? A Medical Sales Rep?</div>
    <div class="abs circle pro-photo p1" role="img" aria-label="Photo of doctors"></div>
    <div class="abs circle pro-photo p2" role="img" aria-label="Photo of a nurse in a headscarf"></div>
    <div class="abs circle pro-photo p3" role="img" aria-label="Photo of a pharmacist"></div>
    <div class="abs circle pro-photo p4" role="img" aria-label="Photo of a medical sales representative"></div>
    <div class="abs pro-text">If you’re interested in a Healthcare Job<br>We’re here to help you grow your <b>CAREER!</b></div>
  </div>

  <div class="abs footer">
    <div class="abs footer-logo"><span class="dot"></span>Vireta</div>
    <div class="abs footer-rule"></div>
    <div class="abs footer-info">
      <div class="tag">Malaysia’s #1 healthcare job site</div>
      <div><span class="social"><i></i>Vireta</span><span class="social"><i></i>viretajobs</span><span class="social"><i></i>@viretajobs</span></div>
      <div>www.vireta-jobs.example</div>
    </div>
  </div>
</section>

</body>
</html>
```